Business card design reauest

2 sided. White on both sides

Martin Oakhurst

Ho Chi Minh, Vietnam

Cell Phone / Whatsapp/ Wechat/Zalo
1-555-382-7194
Moakhurst@kvpartsline.vn
Www.kvpartsline.vn
Www.kvpartsline.com

Industry/Entity Type

Sofa and furniture and kitchen

Contact Information for Business Card

2 sided. White on both sides Martin Oakhurst Ho Chi Minh, Vietnam Cell Phone / Whatsapp/ Wechat/Zalo 1-555-382-7194 Moakhurst@kvpartsline.vn Www.kvpartsline.vn Www.kvpartsline.com

```html
<!DOCTYPE html>
<html lang="en">
<head>
<meta charset="utf-8">
<title>KV Parts Line – Business Card</title>
<link href="https://fonts.googleapis.com/css2?family=Cinzel:wght@500&family=Montserrat:wght@400&display=swap" rel="stylesheet">
<style>
  :root {
    --backdrop: #b9b9b9;
    --card: #ffffff;
    --green: #12a03a;
    --ink: #1f1f1f;
    --muted: #333333;
    --decor-light: #f6f6f6;
    --decor-mid: #ececec;
  }
  * { box-sizing: border-box; margin: 0; padding: 0; }
  html, body { width: 1200px; height: 900px; overflow: hidden; }
  body {
    background: var(--backdrop);
    display: flex;
    flex-direction: column;
    align-items: center;
    justify-content: center;
    gap: 40px;
    font-family: "Montserrat", sans-serif;
  }
  .card {
    position: relative;
    width: 630px;
    height: 360px;
    background: var(--card);
    border-radius: 26px;
    overflow: hidden;
    box-shadow: 0 6px 18px rgba(0,0,0,0.18);
  }
  .card__decor {
    position: absolute;
    top: 0; right: 0;
    width: 330px; height: 100%;
    background: linear-gradient(160deg, var(--decor-light), var(--decor-mid));
    opacity: 0.7;
  }
  .brand {
    position: absolute;
    display: flex;
    align-items: center;
    gap: 12px;
    font-family: "Cinzel", serif;
    font-weight: 500;
    color: var(--green);
    letter-spacing: 2px;
    white-space: nowrap;
  }
  .brand__mark {
    width: 14px; height: 14px;
    background: var(--green);
  }
  .card--front .brand {
    left: 50%; top: 50%;
    transform: translate(-50%, -50%);
    font-size: 44px;
  }
  .card--back .brand {
    left: 40px; top: 70px;
    font-size: 34px;
  }
  .contact-list {
    position: absolute;
    left: 40px; bottom: 34px;
    list-style: none;
    display: flex;
    flex-direction: column;
    gap: 9px;
    font-size: 16px;
    color: var(--muted);
  }
  .contact-list li { display: flex; align-items: center; gap: 10px; }
  .icon {
    width: 24px; height: 24px;
    border-radius: 50%;
    background: var(--green);
    display: flex; align-items: center; justify-content: center;
    flex-shrink: 0;
  }
  .holder {
    position: absolute;
    right: 36px; top: 150px;
    text-align: right;
  }
  .holder__name {
    display: flex;
    align-items: center;
    justify-content: flex-end;
    gap: 10px;
    font-family: "Cinzel", serif;
    font-weight: 500;
    font-size: 22px;
    letter-spacing: 1px;
    color: var(--green);
  }
  .holder__tab { width: 14px; height: 22px; background: var(--green); }
  .channels {
    display: flex;
    justify-content: flex-end;
    gap: 6px;
    margin-top: 16px;
  }
  .holder__phone {
    margin-top: 8px;
    font-size: 18px;
    color: var(--ink);
    letter-spacing: 1px;
  }
</style>
</head>
<body>
  <section class="card card--front">
    <div class="card__decor" role="img" aria-label="Faint grey illustration of a house outline with a hanging lamp and table"></div>
    <div class="brand"><span class="brand__mark"></span>KV Parts Line</div>
  </section>

  <section class="card card--back">
    <div class="card__decor" role="img" aria-label="Faint grey illustration of a house outline with a hanging lamp and table"></div>
    <div class="brand"><span class="brand__mark"></span>KV Parts Line</div>

    <ul class="contact-list">
      <li>
        <span class="icon"><svg width="12" height="14" viewBox="0 0 12 14"><path d="M6 0a5 5 0 0 0-5 5c0 4 5 9 5 9s5-5 5-9a5 5 0 0 0-5-5z" fill="#fff"/><circle cx="6" cy="5" r="2" fill="#12a03a"/></svg></span>
        Ho Chi Minh, Vietnam
      </li>
      <li>
        <span class="icon"><svg width="13" height="10" viewBox="0 0 13 10"><rect x="0.5" y="0.5" width="12" height="9" fill="#fff"/><path d="M0.5 0.5l6 5 6-5" fill="none" stroke="#12a03a" stroke-width="1"/></svg></span>
        Moakhurst@kvpartsline.vn
      </li>
      <li>
        <span class="icon"><svg width="14" height="14" viewBox="0 0 14 14" fill="none" stroke="#fff" stroke-width="1.2"><circle cx="7" cy="7" r="6"/><ellipse cx="7" cy="7" rx="2.6" ry="6"/><path d="M1 7h12M2 4h10M2 10h10"/></svg></span>
        Www.kvpartsline.vn
      </li>
      <li>
        <span class="icon"><svg width="14" height="14" viewBox="0 0 14 14" fill="none" stroke="#fff" stroke-width="1.2"><circle cx="7" cy="7" r="6"/><ellipse cx="7" cy="7" rx="2.6" ry="6"/><path d="M1 7h12M2 4h10M2 10h10"/></svg></span>
        Www.kvpartsline.com
      </li>
    </ul>

    <div class="holder">
      <div class="holder__name">Martin Oakhurst<span class="holder__tab"></span></div>
      <div class="channels">
        <span class="icon"><svg width="9" height="14" viewBox="0 0 9 14"><rect x="0.5" y="0.5" width="8" height="13" rx="1.5" fill="none" stroke="#fff"/><circle cx="4.5" cy="11" r="0.9" fill="#fff"/></svg></span>
        <span class="icon"></span>
        <span class="icon"></span>
        <span class="icon"></span>
      </div>
      <div class="holder__phone">1-555-382-7194</div>
    </div>
  </section>
</body>
</html>
```